Brightpine Heating and Cooling inc

Free System Replacement estimate
Financing available
Indoor Air Quality
high efficiency system
Zorvik, Pictaloom, Kindrafold
website info
Se Habla Espanol
Free second opinion
We service all major brand

Target Market(s)

Hvac Home Services

Industry/Entity Type

Hvac

Font styles to use
Sans Serif
Other font styles liked:
• Vorneq letter

Colors
3377b5
9bcb3c

```html
<!DOCTYPE html>
<html lang="en">
<head>
<meta charset="utf-8">
<title>Brightpine Heating and Cooling inc — Postcard</title>
<link rel="stylesheet" href="https://fonts.googleapis.com/css2?family=Open+Sans:wght@400&family=Poppins:ital,wght@0,500;0,600;0,700;0,800;1,700;1,800&family=Raleway:wght@400;700;800&display=swap">
<style>
  :root {
    --blue: #2e5a87;
    --blue-dark: #234a72;
    --green: #76bc43;
    --ink: #4a5358;
    --muted: #6b7378;
    --panel: #eff1f2;
    --stage: #e8e6e2;
    --white: #ffffff;
  }
  * { margin: 0; padding: 0; box-sizing: border-box; }
  html, body { width: 1200px; height: 2286px; overflow: hidden; }
  body { background: var(--stage); position: relative; }
  .postcard {
    position: absolute;
    left: 60px;
    width: 1080px;
    height: 720px;
    display: block;
    box-shadow: 0 10px 28px rgba(0,0,0,.22);
    background: var(--white);
  }
  .postcard--front { top: 383px; }
  .postcard--back { top: 1183px; }
  .f-raleway { font-family: 'Raleway', sans-serif; }
  .f-poppins { font-family: 'Poppins', sans-serif; }
  .f-open { font-family: 'Open Sans', sans-serif; }
  .brand-name { font-family: 'Raleway', sans-serif; font-weight: 800; fill: var(--blue); }
  .tagline { font-family: 'Raleway', sans-serif; font-size: 19px; fill: var(--blue); }
  .benefit { font-family: 'Poppins', sans-serif; font-weight: 500; font-size: 15.5px; fill: var(--white); }
  .contact-line { font-family: 'Poppins', sans-serif; font-size: 15px; fill: var(--white); }
  .social-name { font-family: 'Poppins', sans-serif; font-weight: 600; font-size: 8.5px; fill: var(--blue); }
  .story-copy { font-family: 'Open Sans', sans-serif; font-size: 12.2px; fill: var(--ink); }
  .service-label { font-family: 'Poppins', sans-serif; font-weight: 600; font-size: 15.5px; fill: var(--white); text-anchor: middle; }
</style>
</head>
<body>

<!-- Front of the postcard -->
<svg class="postcard postcard--front" viewBox="0 0 865 577" xmlns="http://www.w3.org/2000/svg">
  <defs>
    <clipPath id="front-card"><rect width="865" height="577"/></clipPath>
    <clipPath id="front-photo">
      <circle cx="677" cy="288" r="272"/>
      <rect x="677" y="0" width="188" height="505"/>
    </clipPath>
    <clipPath id="front-arc-top"><rect x="0" y="0" width="677" height="272"/></clipPath>
    <clipPath id="front-arc-bottom"><rect x="0" y="300" width="677" height="277"/></clipPath>
    <linearGradient id="front-photo-tone" x1="0" y1="0" x2="1" y2="1">
      <stop offset="0" stop-color="#cfd4d8"/>
      <stop offset=".45" stop-color="#7f8a93"/>
      <stop offset="1" stop-color="#3d4a57"/>
    </linearGradient>
  </defs>

  <g clip-path="url(#front-card)">
    <rect class="card-bg" width="865" height="577" fill="var(--white)"/>

    <!-- benefits band -->
    <rect class="benefits-band" x="0" y="275" width="700" height="230" fill="var(--blue)"/>
    <!-- contact strip -->
    <polygon class="contact-strip" points="240,505 720,505 720,577 226,577" fill="var(--green)"/>

    <!-- ring and photo -->
    <circle class="ring-gap" cx="677" cy="288" r="301" fill="var(--white)"/>
    <circle class="ring-green" cx="677" cy="288" r="287" fill="none" stroke="var(--green)" stroke-width="14" clip-path="url(#front-arc-top)"/>
    <circle class="ring-blue" cx="677" cy="288" r="287" fill="none" stroke="var(--blue)" stroke-width="14" clip-path="url(#front-arc-bottom)"/>
    <g role="img" aria-label="Photo of a technician in a hard hat testing an outdoor air conditioning unit with a meter" clip-path="url(#front-photo)">
      <rect x="380" y="0" width="485" height="505" fill="url(#front-photo-tone)"/>
    </g>

    <!-- brand -->
    <g class="brand">
      <circle cx="60" cy="86" r="24" fill="var(--green)"/>
      <text class="brand-name" x="94" y="104" font-size="50">Brightpine</text>
      <text class="brand-name" x="96" y="138" font-size="18">Heating &amp; Cooling INC.</text>
    </g>

    <!-- tagline -->
    <rect x="34" y="184" width="3" height="76" fill="var(--green)"/>
    <text class="tagline" x="48" y="203">Quality That is Guaranted</text>
    <text class="tagline" x="48" y="229"><tspan font-weight="800">Heating</tspan> and <tspan font-weight="800" fill="var(--green)">Air Conditioning</tspan></text>
    <text class="tagline" x="48" y="255" font-weight="800" fill="#555">Comfort Specialist</text>

    <!-- benefits -->
    <g class="benefit-list">
      <g stroke="rgba(255,255,255,.18)" stroke-width="1">
        <line x1="80" y1="342" x2="340" y2="342"/>
        <line x1="80" y1="393" x2="370" y2="393"/>
        <line x1="80" y1="443" x2="380" y2="443"/>
      </g>
      <g fill="#e9ecee" stroke="#ffffff" stroke-width="2">
        <polygon points="55,297 72,307 72,327 55,337 38,327 38,307"/>
        <polygon points="55,347 72,357 72,377 55,387 38,377 38,357"/>
        <polygon points="55,398 72,408 72,428 55,438 38,428 38,408"/>
        <polygon points="55,451 72,461 72,481 55,491 38,481 38,461"/>
      </g>
      <g fill="none" stroke="var(--blue)" stroke-width="1.6">
        <circle cx="55" cy="317" r="7"/><circle cx="55" cy="317" r="2.5"/>
        <circle cx="57" cy="364" r="5"/><path d="M46 375 l6 -4 h8 l5 4"/>
        <rect x="48" y="411" width="14" height="13"/><path d="M51 414 v7 M55 414 v7 M59 414 v7"/>
        <circle cx="55" cy="471" r="8"/><path d="M55 466 v5 h4"/>
      </g>
      <text class="benefit" x="92" y="309">Free System</text>
      <text class="benefit" x="92" y="330">Replacement estimate</text>
      <text class="benefit" x="92" y="372">Financing available</text>
      <text class="benefit" x="92" y="423">Indoor Air Quality</text>
      <text class="benefit" x="92" y="466">Calderra Systems high efficiency</text>
      <text class="benefit" x="92" y="487">on the background</text>
    </g>

    <!-- emergency badge -->
    <g class="emergency">
      <path d="M96 518 a18 18 0 1 1 -2 34" fill="none" stroke="var(--blue)" stroke-width="2"/>
      <text x="36" y="562" font-family="Poppins, sans-serif" font-weight="800" font-style="italic" font-size="32" fill="var(--blue)" letter-spacing="-2">24<tspan fill="var(--green)">/</tspan>7</text>
      <text x="124" y="545" font-family="Poppins, sans-serif" font-weight="700" font-style="italic" font-size="11.5" fill="var(--green)">EMERGENCY</text>
      <text x="124" y="559" font-family="Poppins, sans-serif" font-weight="700" font-style="italic" font-size="11.5" fill="var(--blue)">SERVICE</text>
    </g>

    <!-- contact -->
    <g class="contact">
      <circle cx="255" cy="533" r="6" fill="none" stroke="#fff" stroke-width="1.4"/>
      <path d="M252 530 q1 5 6 6" fill="none" stroke="#fff" stroke-width="1.4"/>
      <text class="contact-line" x="267" y="538">Call Today <tspan font-weight="700">407-555-0148</tspan></text>
      <circle cx="255" cy="557" r="6" fill="none" stroke="#fff" stroke-width="1.4"/>
      <path d="M249 557 h12 M255 551 v12" stroke="#fff" stroke-width="1"/>
      <text class="contact-line" x="267" y="562">www.<tspan font-weight="700">brightpine365</tspan>.com</text>
    </g>

    <!-- listings and licence -->
    <g class="listings">
      <text class="social-name" x="592" y="548">Zorvik</text>
      <rect x="625" y="536" width="1" height="16" fill="var(--blue)"/>
      <text class="social-name" x="631" y="548">Pictaloom</text>
      <rect x="676" y="536" width="1" height="16" fill="var(--blue)"/>
      <text class="social-name" x="682" y="548">Kindrafold</text>
      <rect x="738" y="531" width="124" height="27" rx="13.5" fill="var(--green)"/>
      <text x="800" y="549" text-anchor="middle" font-family="Poppins, sans-serif" font-weight="700" font-size="10.5" fill="#fff">LIC# CAC1049372</text>
    </g>
  </g>
</svg>

<!-- Back of the postcard -->
<svg class="postcard postcard--back" viewBox="0 0 865 577" xmlns="http://www.w3.org/2000/svg">
  <defs>
    <clipPath id="back-card"><rect width="865" height="577"/></clipPath>
    <clipPath id="back-panel"><circle cx="240" cy="288" r="285"/></clipPath>
    <clipPath id="back-arc-top"><rect x="240" y="0" width="625" height="272"/></clipPath>
    <clipPath id="back-arc-bottom"><rect x="240" y="300" width="625" height="277"/></clipPath>
  </defs>

  <g clip-path="url(#back-card)">
    <rect width="865" height="577" fill="var(--white)"/>
    <circle class="story-panel" cx="240" cy="288" r="285" fill="var(--panel)"/>
    <circle class="ring-green" cx="240" cy="288" r="298" fill="none" stroke="var(--green)" stroke-width="14" clip-path="url(#back-arc-top)"/>
    <circle class="ring-blue" cx="240" cy="288" r="298" fill="none" stroke="var(--blue)" stroke-width="14" clip-path="url(#back-arc-bottom)"/>

    <!-- story -->
    <text x="29" y="44" font-family="Raleway, sans-serif" font-size="22" fill="var(--muted)">Our Story</text>
    <text x="28" y="84" font-family="Raleway, sans-serif" font-size="33" fill="#555">Meet <tspan font-weight="800">Brightpine</tspan></text>
    <g class="story-copy">
      <text x="29" y="111">As a family owned and operated company, we take pride in</text>
      <text x="29" y="130">the dedication of our HVAC services. We understand that time</text>
      <text x="29" y="149">and cost are crucial, so we strive to go above and beyond our</text>
      <text x="29" y="168">client’s expectations. Our goal is to address every call</text>
      <text x="29" y="187">promptly and with professionalism. Due to our fair rates,</text>
      <text x="29" y="206">quality of work and outstanding services we have been able</text>
      <text x="29" y="225">to help families meet their comfort needs. For our customers</text>
      <text x="29" y="244">peace of mind, we offer valuable money saving service and</text>
      <text x="29" y="263">maintenance contracts. Please call for additional details.</text>
    </g>

    <!-- services -->
    <g clip-path="url(#back-panel)">
      <rect class="services-band" x="0" y="286" width="600" height="149" fill="var(--green)"/>
    </g>
    <polygon points="152,286 357,286 343,320 166,320" fill="var(--blue)"/>
    <text x="252" y="313" text-anchor="middle" font-family="Raleway, sans-serif" font-size="22" fill="#fff">Our <tspan font-weight="800">Services</tspan></text>
    <g stroke="rgba(255,255,255,.75)" stroke-width="1">
      <line x1="158" y1="336" x2="158" y2="425"/>
      <line x1="313" y1="336" x2="313" y2="425"/>
    </g>
    <g fill="none" stroke="#fff" stroke-width="1.6">
      <rect x="66" y="340" width="26" height="24" rx="2"/>
      <path d="M66 347 h26 M72 336 v7 M86 336 v7"/>
      <path d="M226 338 l20 22 M246 338 l-20 22"/>
      <circle cx="387" cy="352" r="14"/>
      <text x="387" y="356" text-anchor="middle" font-family="Poppins, sans-serif" font-size="8" fill="#fff" stroke="none">24/7</text>
    </g>
    <text class="service-label" x="80" y="392">Annual</text>
    <text class="service-label" x="80" y="410">inspections</text>
    <text class="service-label" x="236" y="393">A/C</text>
    <text class="service-label" x="236" y="412">installation</text>
    <text class="service-label" x="387" y="389">Service</text>
    <text class="service-label" x="387" y="408">and repair</text>

    <polygon points="45,435 384,435 364,470 66,470" fill="var(--blue)"/>
    <text x="226" y="460" text-anchor="middle" font-family="Raleway, sans-serif" font-size="21" fill="#fff">Schedule an <tspan font-weight="800">Appointment</tspan></text>

    <!-- contact -->
    <g fill="none" stroke="var(--blue)" stroke-width="2">
      <path d="M70 498 q0 14 14 16 l3 -4 -5 -4 -3 2 q-4 -2 -5 -6 l2 -3 -4 -5 z" fill="var(--blue)" stroke="none"/>
      <circle cx="78" cy="542" r="8"/>
      <path d="M70 542 h16 M78 534 v16" stroke-width="1"/>
    </g>
    <text x="97" y="518" font-family="Poppins, sans-serif" font-weight="700" font-size="35" fill="var(--green)">407-555-0148</text>
    <text x="99" y="550" font-family="Poppins, sans-serif" font-size="20" fill="var(--blue)">www.<tspan font-weight="700">brightpine365</tspan>.com</text>

    <!-- brand -->
    <g class="brand">
      <circle cx="527" cy="82" r="16" fill="var(--green)"/>
      <text class="brand-name" x="550" y="93" font-size="30">Brightpine</text>
      <text class="brand-name" x="551" y="112" font-size="11">Heating &amp; Cooling INC.</text>
    </g>

    <!-- mailing area -->
    <rect class="stamp-box" x="732" y="30" width="106" height="107" fill="none" stroke="#333" stroke-width="1.2"/>
    <g stroke="#444" stroke-width="1">
      <line x1="596" y1="311" x2="838" y2="311"/>
      <line x1="596" y1="370" x2="838" y2="370"/>
      <line x1="596" y1="429" x2="838" y2="429"/>
    </g>

    <!-- address line -->
    <path d="M441 541 a4.5 4.5 0 0 1 9 0 q0 4 -4.5 10 q-4.5 -6 -4.5 -10 z" fill="var(--green)"/>
    <text x="453" y="554" font-family="Open Sans, sans-serif" font-size="14.5" fill="#444">Pinecrest, FL 34700</text>
    <rect x="590" y="540" width="1.5" height="18" fill="var(--blue)"/>
    <rect x="598" y="545" width="10" height="7" fill="var(--green)"/>
    <text x="612" y="554" font-family="Open Sans, sans-serif" font-size="14.5" fill="#444">sam@<tspan fill="var(--green)">brightpine365</tspan>.com</text>
  </g>
</svg>

</body>
</html>
```